Create banners that convert viewers into buyers!

We provide Online Marketing Solutions for small to medium size businesses from web design, Local SEO, Pay-Per-Click, Social Media and Content Marketing. We've been helping local businesses since 2009 and offer a very high level of service that is rarely matched.

Really like to stay colors of logo like banner ad ideas 2 sample.

Would also like to use a photo of a responsive web design as attached image. (you may use a different layout as image provided may be to big for some dimensions)

Sizes needed:
728x90
300x250
480x60

Add Slogan: We Drive Traffic & Phone Calls!

Slogan: We Drive Phone Calls & Conversions

Target Market(s)

Small to Medium Size businesses: Main businesses we work with are Home Improvement, Lawyers & Physicians

Industry/Entity Type

Marketing

```html
<!DOCTYPE html>
<html lang="en">
<head>
<meta charset="utf-8">
<title>Northline Marketing – Banner Set</title>
<link rel="stylesheet" href="https://fonts.googleapis.com/css2?family=Arimo:wght@400;700&family=Roboto+Condensed:wght@700&display=swap">
<style>
  :root {
    --brand-blue: #1b6fb8;
    --chip-top: #2a86e0;
    --chip-bottom: #0d55b0;
    --stage-black: #020305;
    --glow-blue: #0a5fb8;
    --button-top: #ffd23a;
    --button-bottom: #f39a00;
    --button-edge: #c97800;
    --ink: #111111;
    --frame: #8f8f8f;
    --paper: #ffffff;
    --note-grey: #b9b9b9;
    --visual-a: #6b7d94;
    --visual-b: #1e2a3a;
  }
  * { box-sizing: border-box; margin: 0; padding: 0; }
  html, body { width: 1200px; height: 1094px; overflow: hidden; background: var(--paper); }
  body { font-family: "Arimo", Arial, sans-serif; }

  .board { position: absolute; left: 0; top: 0; width: 755px; height: 689px; transform: scale(1.5894); transform-origin: 0 0; }

  .banner { position: absolute; background: var(--paper); border: 1px solid var(--frame); overflow: hidden; }
  .banner--medium { width: 301px; height: 251px; }
  .banner--leader { width: 729px; height: 91px; }
  .banner--mobile { width: 471px; height: 61px; }

  .stage { position: absolute; background:
      radial-gradient(ellipse at 30% 60%, rgba(40,140,255,.75) 0%, rgba(10,95,184,.45) 30%, rgba(2,3,5,0) 65%),
      var(--stage-black); }
  .visual { position: absolute; border-radius: 3px;
      background: linear-gradient(135deg, var(--visual-a), var(--visual-b) 70%); box-shadow: 0 0 8px rgba(60,170,255,.9); }

  .brand { position: absolute; color: var(--brand-blue); font-weight: 700; text-align: center; line-height: 1; }
  .brand__name { display: block; }
  .brand__tag { display: block; letter-spacing: .35em; }
  .brand__dot { display: inline-block; border-radius: 50%; background: var(--brand-blue); }

  .headline { position: absolute; color: #fff; font-weight: 700; text-align: center; text-shadow: 0 1px 3px #000; }
  .headline--condensed { font-family: "Roboto Condensed", "Arial Narrow", sans-serif; white-space: nowrap; letter-spacing: -0.2px; }

  .chip { position: absolute; color: #fff; background: linear-gradient(var(--chip-top), var(--chip-bottom));
      border-radius: 1px; display: flex; align-items: center; white-space: nowrap; overflow: hidden; }
  .chip::before { content: ""; flex: none; border-style: solid; border-color: transparent transparent transparent #fff; margin-right: .45em; }
  .chip--lg { height: 17px; font-size: 12.5px; padding-left: 7px; }
  .chip--lg::before { border-width: 4px 0 4px 6px; }
  .chip--md { height: 15px; font-size: 12px; padding-left: 8px; }
  .chip--md::before { border-width: 4px 0 4px 6px; }
  .chip--sm { height: 10px; font-size: 7px; padding-left: 4px; }
  .chip--sm::before { border-width: 2.5px 0 2.5px 4px; }
  .chip--long { font-size: 10.5px; }

  .cta { position: absolute; display: flex; align-items: center; justify-content: center; gap: 4px;
      background: linear-gradient(var(--button-top), var(--button-bottom)); border: 1px solid var(--button-edge);
      border-radius: 4px; color: var(--ink); font-weight: 700; white-space: nowrap; }
  .cta svg { flex: none; }
  .site { position: absolute; color: var(--ink); white-space: nowrap; }

  .notch { position: absolute; width: 0; height: 0; border-style: solid; }

  .note { position: absolute; left: 543px; top: 572px; color: var(--note-grey); font-size: 19px; }
</style>
</head>
<body>
<main class="board">

  <!-- 300x250, cursor button -->
  <section class="banner banner--medium" style="left:69px; top:33px;">
    <div class="brand" style="left:0; top:6px; width:300px;">
      <span class="brand__name" style="font-size:25px;"><span class="brand__dot" style="width:6px;height:6px;vertical-align:top;margin-right:3px;"></span>NORTHLINE</span>
      <span class="brand__tag" style="font-size:8px; margin-top:2px;">MARKETING</span>
    </div>
    <div class="stage" style="left:0; top:45px; width:300px; height:166px;"></div>
    <div class="notch" style="left:143px; top:44px; border-width:8px 7px 0 7px; border-color:var(--paper) transparent transparent transparent;"></div>
    <h2 class="headline" style="left:0; top:52px; width:300px; font-size:26px; line-height:28px;">We Drive Traffic &amp;<br>Phone Calls!</h2>
    <div class="visual" role="img" aria-label="Responsive website shown on desktop, tablet and phone" style="left:6px; top:108px; width:166px; height:98px;"></div>
    <div class="chip chip--lg" style="left:178px; top:117px; width:112px;">Web Design</div>
    <div class="chip chip--lg" style="left:178px; top:136px; width:112px;">Local SEO</div>
    <div class="chip chip--lg" style="left:178px; top:155px; width:112px;">Pay-Per-Click</div>
    <div class="chip chip--lg" style="left:178px; top:174px; width:112px;">Social Media</div>
    <div class="chip chip--lg chip--long" style="left:178px; top:193px; width:112px;">Content Marketing</div>
    <div class="site" style="left:26px; top:231px; font-size:12px;">www.yoursite.com</div>
    <div class="cta" style="left:180px; top:216px; width:114px; height:30px; font-size:17px;">
      <svg width="12" height="16" viewBox="0 0 12 16"><path d="M1 1 L1 13 L4 10 L6.5 15 L8.5 14 L6 9 L10.5 9 Z" fill="#111"/></svg>Learn More
    </div>
  </section>

  <!-- 300x250, circle button -->
  <section class="banner banner--medium" style="left:382px; top:33px;">
    <div class="brand" style="left:0; top:6px; width:300px;">
      <span class="brand__name" style="font-size:25px;"><span class="brand__dot" style="width:6px;height:6px;vertical-align:top;margin-right:3px;"></span>NORTHLINE</span>
      <span class="brand__tag" style="font-size:8px; margin-top:2px;">MARKETING</span>
    </div>
    <div class="stage" style="left:0; top:45px; width:300px; height:166px;"></div>
    <div class="notch" style="left:143px; top:44px; border-width:8px 7px 0 7px; border-color:var(--paper) transparent transparent transparent;"></div>
    <h2 class="headline" style="left:0; top:52px; width:300px; font-size:26px; line-height:28px;">We Drive Traffic &amp;<br>Phone Calls!</h2>
    <div class="visual" role="img" aria-label="Responsive website shown on desktop, tablet and phone" style="left:6px; top:108px; width:166px; height:98px;"></div>
    <div class="chip chip--lg" style="left:178px; top:117px; width:112px;">Web Design</div>
    <div class="chip chip--lg" style="left:178px; top:136px; width:112px;">Local SEO</div>
    <div class="chip chip--lg" style="left:178px; top:155px; width:112px;">Pay-Per-Click</div>
    <div class="chip chip--lg" style="left:178px; top:174px; width:112px;">Social Media</div>
    <div class="chip chip--lg chip--long" style="left:178px; top:193px; width:112px;">Content Marketing</div>
    <div class="site" style="left:26px; top:231px; font-size:12px;">www.yoursite.com</div>
    <div class="cta" style="left:170px; top:216px; width:124px; height:30px; font-size:17px;">
      Learn More<svg width="20" height="20" viewBox="0 0 20 20"><circle cx="10" cy="10" r="9" fill="#17408f" stroke="#d23a1c" stroke-width="1.5"/><path d="M8 5.5 L13 10 L8 14.5 Z" fill="#ffb300"/></svg>
    </div>
  </section>

  <!-- 728x90, circle button -->
  <section class="banner banner--leader" style="left:12px; top:299px;">
    <div class="brand" style="left:0; top:30px; width:158px;">
      <span class="brand__name" style="font-size:22px;">NORTHLINE</span>
      <span class="brand__tag" style="font-size:8px; margin-top:3px;">MARKETING</span>
    </div>
    <div class="stage" style="left:158px; top:0; width:442px; height:90px;"></div>
    <div class="notch" style="left:157px; top:38px; border-width:7px 0 7px 8px; border-color:transparent transparent transparent var(--paper);"></div>
    <div class="visual" role="img" aria-label="Responsive website shown on desktop, tablet and phone" style="left:168px; top:4px; width:164px; height:82px;"></div>
    <h2 class="headline headline--condensed" style="left:336px; top:5px; width:262px; font-size:21px; line-height:26px;">We Drive Traffic &amp; Phone Calls!</h2>
    <div class="chip chip--md" style="left:338px; top:37px; width:113px;">Web Design</div>
    <div class="chip chip--md" style="left:460px; top:37px; width:113px;">Local SEO</div>
    <div class="chip chip--md" style="left:338px; top:55px; width:113px;">Pay-Per-Click</div>
    <div class="chip chip--md" style="left:460px; top:55px; width:113px;">Social Media</div>
    <div class="chip chip--md chip--long" style="left:388px; top:73px; width:112px;">Content Marketing</div>
    <div class="cta" style="left:602px; top:32px; width:123px; height:28px; font-size:16px;">
      Learn More<svg width="19" height="19" viewBox="0 0 20 20"><circle cx="10" cy="10" r="9" fill="#17408f" stroke="#d23a1c" stroke-width="1.5"/><path d="M8 5.5 L13 10 L8 14.5 Z" fill="#ffb300"/></svg>
    </div>
    <div class="site" style="left:602px; top:64px; width:123px; text-align:center; font-size:12px;">www.yoursite.com</div>
  </section>

  <!-- 728x90, cursor button -->
  <section class="banner banner--leader" style="left:12px; top:405px;">
    <div class="brand" style="left:0; top:30px; width:158px;">
      <span class="brand__name" style="font-size:22px;">NORTHLINE</span>
      <span class="brand__tag" style="font-size:8px; margin-top:3px;">MARKETING</span>
    </div>
    <div class="stage" style="left:158px; top:0; width:442px; height:90px;"></div>
    <div class="notch" style="left:157px; top:38px; border-width:7px 0 7px 8px; border-color:transparent transparent transparent var(--paper);"></div>
    <div class="visual" role="img" aria-label="Responsive website shown on desktop, tablet and phone" style="left:168px; top:4px; width:164px; height:82px;"></div>
    <h2 class="headline headline--condensed" style="left:336px; top:5px; width:262px; font-size:21px; line-height:26px;">We Drive Traffic &amp; Phone Calls!</h2>
    <div class="chip chip--md" style="left:338px; top:37px; width:113px;">Web Design</div>
    <div class="chip chip--md" style="left:460px; top:37px; width:113px;">Local SEO</div>
    <div class="chip chip--md" style="left:338px; top:55px; width:113px;">Pay-Per-Click</div>
    <div class="chip chip--md" style="left:460px; top:55px; width:113px;">Social Media</div>
    <div class="chip chip--md chip--long" style="left:388px; top:73px; width:112px;">Content Marketing</div>
    <div class="cta" style="left:606px; top:30px; width:114px; height:30px; font-size:16px;">
      <svg width="12" height="16" viewBox="0 0 12 16"><path d="M1 1 L1 13 L4 10 L6.5 15 L8.5 14 L6 9 L10.5 9 Z" fill="#111"/></svg>Learn More
    </div>
    <div class="site" style="left:602px; top:64px; width:123px; text-align:center; font-size:12px;">www.yoursite.com</div>
  </section>

  <!-- 480x60, circle button -->
  <section class="banner banner--mobile" style="left:12px; top:515px;">
    <div class="brand" style="left:0; top:18px; width:100px;">
      <span class="brand__name" style="font-size:14px;">NORTHLINE</span>
      <span class="brand__tag" style="font-size:5.5px; margin-top:2px;">MARKETING</span>
    </div>
    <div class="stage" style="left:100px; top:0; width:289px; height:60px;"></div>
    <div class="visual" role="img" aria-label="Responsive website shown on desktop, tablet and phone" style="left:106px; top:3px; width:104px; height:54px;"></div>
    <h2 class="headline headline--condensed" style="left:214px; top:3px; width:172px; font-size:13.5px; line-height:17px;">We Drive Traffic &amp; Phone Calls!</h2>
    <div class="chip chip--sm" style="left:218px; top:25px; width:76px;">Web Design</div>
    <div class="chip chip--sm" style="left:297px; top:25px; width:76px;">Local SEO</div>
    <div class="chip chip--sm" style="left:218px; top:37px; width:76px;">Pay-Per-Click</div>
    <div class="chip chip--sm" style="left:297px; top:37px; width:76px;">Social Media</div>
    <div class="chip chip--sm" style="left:251px; top:48px; width:76px;">Content Marketing</div>
    <div class="cta" style="left:389px; top:21px; width:79px; height:19px; font-size:10px; border-radius:3px; gap:3px;">
      Learn More<svg width="12" height="12" viewBox="0 0 20 20"><circle cx="10" cy="10" r="9" fill="#17408f" stroke="#d23a1c" stroke-width="1.5"/><path d="M8 5.5 L13 10 L8 14.5 Z" fill="#ffb300"/></svg>
    </div>
    <div class="site" style="left:389px; top:43px; width:79px; text-align:center; font-size:8px;">www.yoursite.com</div>
  </section>

  <!-- 480x60, cursor button -->
  <section class="banner banner--mobile" style="left:12px; top:586px;">
    <div class="brand" style="left:0; top:18px; width:100px;">
      <span class="brand__name" style="font-size:14px;">NORTHLINE</span>
      <span class="brand__tag" style="font-size:5.5px; margin-top:2px;">MARKETING</span>
    </div>
    <div class="stage" style="left:100px; top:0; width:289px; height:60px;"></div>
    <div class="visual" role="img" aria-label="Responsive website shown on desktop, tablet and phone" style="left:106px; top:3px; width:104px; height:54px;"></div>
    <h2 class="headline headline--condensed" style="left:214px; top:3px; width:172px; font-size:13.5px; line-height:17px;">We Drive Traffic &amp; Phone Calls!</h2>
    <div class="chip chip--sm" style="left:218px; top:25px; width:76px;">Web Design</div>
    <div class="chip chip--sm" style="left:297px; top:25px; width:76px;">Local SEO</div>
    <div class="chip chip--sm" style="left:218px; top:37px; width:76px;">Pay-Per-Click</div>
    <div class="chip chip--sm" style="left:297px; top:37px; width:76px;">Social Media</div>
    <div class="chip chip--sm" style="left:251px; top:48px; width:76px;">Content Marketing</div>
    <div class="cta" style="left:391px; top:20px; width:74px; height:20px; font-size:10px; border-radius:3px; gap:3px;">
      <svg width="8" height="11" viewBox="0 0 12 16"><path d="M1 1 L1 13 L4 10 L6.5 15 L8.5 14 L6 9 L10.5 9 Z" fill="#111"/></svg>Learn More
    </div>
    <div class="site" style="left:389px; top:43px; width:79px; text-align:center; font-size:8px;">www.yoursite.com</div>
  </section>

  <p class="note">Button Changed.</p>
</main>
</body>
</html>
```